Postcard Project

I need a postcard designed 6X9 in size printed full color
Will need in the end a high resolution print ready file with crop marks
See instructions in word doc

```html
<!DOCTYPE html>
<html lang="en">
<head>
<meta charset="utf-8">
<title>Drinkware Promotion Postcard</title>
<link rel="stylesheet" href="https://fonts.googleapis.com/css2?family=Anton&family=Bebas+Neue&family=Roboto+Condensed:wght@300;400&family=Roboto:wght@400&display=swap">
<style>
  :root {
    --red: #ff0000;
    --black: #000000;
    --white: #ffffff;
    --page: #ececec;
    --ink: #111111;
  }
  * { margin: 0; padding: 0; box-sizing: border-box; }
  html, body { width: 1200px; height: 872px; overflow: hidden; background: var(--page); }
  .postcard {
    position: absolute; left: 100px; top: 102px; width: 1000px; height: 669px;
    background: var(--white); overflow: hidden;
  }
  .headline {
    position: absolute; left: 0; top: 0; width: 1000px; height: 131px;
    background: var(--red); color: var(--white);
    font-family: "Bebas Neue", sans-serif; font-weight: 400;
  }
  .headline-offer { position: absolute; left: 30px; top: 10px; font-size: 50px; line-height: 1; white-space: nowrap; }
  .headline-code { position: absolute; left: 30px; top: 58px; font-size: 76px; line-height: 1; white-space: nowrap; }

  .product { position: absolute; width: 240px; text-align: center; }
  .product-photo { display: block; margin: 0 auto; border-radius: 8px; }
  .product-code {
    position: absolute; left: 0; width: 240px; text-align: center;
    font-family: "Roboto Condensed", sans-serif; font-weight: 400; font-size: 18.5px; color: var(--ink); white-space: nowrap;
  }

  .referral {
    position: absolute; left: 0; top: 441px; width: 503px; height: 183px;
    background: var(--red); color: var(--white);
    font-family: "Anton", sans-serif;
  }
  .referral p { position: absolute; left: 26px; white-space: nowrap; line-height: 1; }
  .referral .dark { color: var(--black); }
  .referral-title { top: 10px; font-size: 25px; }
  .referral-title .dark { font-size: 39px; }
  .referral-body { font-size: 25.5px; }

  .first-purchase {
    position: absolute; left: 503px; top: 441px; width: 497px; height: 183px;
    background: var(--black); text-align: center; font-family: "Anton", sans-serif;
  }
  .first-purchase p { position: absolute; left: 0; width: 497px; line-height: 1; white-space: nowrap; }
  .first-amount { top: 2px; font-size: 71px; color: var(--red); }
  .first-detail { top: 71px; font-size: 24.5px; color: var(--white); }
  .first-code { top: 97px; font-size: 38px; color: var(--red); }
  .first-note { top: 146px; font-size: 24px; color: var(--white); }

  .footer { position: absolute; left: 0; top: 624px; width: 1000px; height: 45px; }
  .footer svg { position: absolute; left: 0; top: 0; }
  .address {
    position: absolute; left: 59px; top: 0; font-family: "Roboto", sans-serif;
    font-size: 37px; color: var(--white); line-height: 1.2; white-space: nowrap;
  }
  .footer-tag {
    position: absolute; left: 560px; width: 380px; top: 2px; text-align: center;
    font-family: "Anton", sans-serif; font-size: 31px; color: var(--white); line-height: 1.2; white-space: nowrap;
  }
</style>
</head>
<body>
<main class="postcard">
  <header class="headline">
    <h1 class="headline-offer">DRINKWARE - $50 OFF ON YOUR DRINKWARE ORDER OVER $500</h1>
    <p class="headline-code">PROMO CODE DRINK GOOD TILL 9/30/25</p>
  </header>

  <section class="product" style="left:34px;top:138px">
    <svg class="product-photo" role="img" aria-label="Silver twisted stainless tumbler with clear lid" width="60" height="106"><rect width="60" height="106" rx="10" fill="#cfd2d4"/></svg>
    <p class="product-code" style="top:117px">DW-101SL_B_BACK Black</p>
  </section>
  <section class="product" style="left:275px;top:148px">
    <svg class="product-photo" role="img" aria-label="White camp mug with lid" width="90" height="84"><rect width="90" height="84" rx="8" fill="#eeeeee"/></svg>
    <p class="product-code" style="top:107px">DW-102WH_A_BACK Full Color</p>
  </section>
  <section class="product" style="left:495px;top:138px">
    <svg class="product-photo" role="img" aria-label="Red metal water bottle with loop cap" width="30" height="106"><rect width="30" height="106" rx="8" fill="#c8312c"/></svg>
    <p class="product-code" style="top:117px">DW-103RD_B_BACK White</p>
  </section>
  <section class="product" style="left:733px;top:142px">
    <svg class="product-photo" role="img" aria-label="Black ceramic mug" width="98" height="88"><rect width="98" height="88" rx="14" fill="#1e1e1e"/></svg>
    <p class="product-code" style="top:113px">DW-104BK_B_FR_1276 White</p>
  </section>

  <section class="product" style="left:34px;top:288px">
    <svg class="product-photo" role="img" aria-label="White mug with speckled sand base" width="92" height="102"><rect width="92" height="102" rx="12" fill="#d9d2c0"/></svg>
    <p class="product-code" style="top:117px">DW-105WH_B_FR_4559 Full</p>
  </section>
  <section class="product" style="left:275px;top:287px">
    <svg class="product-photo" role="img" aria-label="Red plastic stadium cup" width="66" height="96"><rect width="66" height="96" rx="8" fill="#d8201c"/></svg>
    <p class="product-code" style="top:118px">DW-106RD_B_FR Black</p>
  </section>
  <section class="product" style="left:495px;top:282px">
    <svg class="product-photo" role="img" aria-label="Blue plastic sport bottle" width="38" height="112"><rect width="38" height="112" rx="8" fill="#1f5fc8"/></svg>
    <p class="product-code" style="top:123px">DW-107RBL_B__7859White</p>
  </section>
  <section class="product" style="left:733px;top:284px">
    <svg class="product-photo" role="img" aria-label="White tumbler with cork base and black lid" width="46" height="106"><rect width="46" height="106" rx="8" fill="#e8e2dc"/></svg>
    <p class="product-code" style="top:121px">DW-108WH_B_FR_7573Black</p>
  </section>

  <section class="referral">
    <p class="referral-title">REFER a Friend <span class="dark">GIVE $100, GET $100</span></p>
    <p class="referral-body" style="top:55px">Give your friends $100 off their first purchase</p>
    <p class="referral-body" style="top:86px">(over $500) and receive a <span class="dark">$100 discount</span></p>
    <p class="referral-body" style="top:117px">on any order (over <span class="dark">$500</span>).</p>
    <p class="referral-body" style="top:148px">Promo Code REFER</p>
  </section>

  <section class="first-purchase">
    <p class="first-amount">$150 off</p>
    <p class="first-detail">your first department purchase of $500</p>
    <p class="first-code">Promo Code FIRST150</p>
    <p class="first-note">Promotions cannot be combined</p>
  </section>

  <footer class="footer">
    <svg width="1000" height="45" viewBox="0 0 1000 45">
      <rect width="1000" height="45" fill="var(--white)"/>
      <polygon points="0,1 486,1 510,45 0,45" fill="var(--black)"/>
      <polygon points="500,1 1000,1 1000,45 522,45" fill="var(--red)"/>
      <path d="M24 8a11 11 0 0 1 11 11c0 8-11 20-11 20S13 27 13 19A11 11 0 0 1 24 8z" fill="var(--white)"/>
      <circle cx="24" cy="19" r="4" fill="var(--black)"/>
    </svg>
    <p class="address">Address line here</p>
    <p class="footer-tag">1st purchase &amp; referral</p>
  </footer>
</main>
</body>
</html>
```